construction co.logo(ie.highway,heavy equip)

need a design for a new construction company in washington state,office is located on the water (beach front)also use a 1952 dunmore keel avalis as portable office,or the standard bold construction type logo's,these are just thoughts and not necassarily direction

Target Market(s)

I will be working as a sub to much larger general contractors and am looking for a strong,stable appearance.

Industry/Entity Type

Construction

```html
<!DOCTYPE html>
<html lang="en">
<head>
<meta charset="utf-8">
<title>keelbuild business cards</title>
<link rel="stylesheet" href="https://fonts.googleapis.com/css2?family=Jost:wght@400;500&display=swap">
<style>
  :root {
    --page: #e9e7e3;
    --charcoal: #2b2b2c;
    --charcoal-light: #3a3a3b;
    --charcoal-dark: #1f1f20;
    --hazard-yellow: #f5c400;
    --hazard-deep: #d9a900;
    --silver-light: #d9dadb;
    --silver: #a9abad;
    --silver-dark: #8a8c8e;
    --white: #ffffff;
    --ink: #2a2a2a;
  }
  * { margin: 0; padding: 0; box-sizing: border-box; }
  html, body { width: 1200px; height: 900px; overflow: hidden; }
  body {
    background: var(--page);
    font-family: "Jost", sans-serif;
    position: relative;
  }
  .card {
    position: absolute;
    width: 560px;
    height: 320px;
    overflow: hidden;
    box-shadow: 0 10px 24px rgba(0,0,0,0.22);
  }
  .accent-band {
    position: absolute;
    left: 0; right: 0;
    height: 14px;
    background: linear-gradient(90deg, var(--hazard-deep), var(--hazard-yellow) 50%, var(--hazard-deep));
  }

  /* contact side */
  .card--contact { left: 580px; top: 110px; }
  .contact-top {
    position: absolute; left: 0; top: 0; right: 0; height: 190px;
    background: linear-gradient(160deg, var(--charcoal-light) 0%, var(--charcoal) 45%, var(--charcoal-dark) 100%);
  }
  .contact-top .accent-band { top: 176px; }
  .contact-bottom {
    position: absolute; left: 0; top: 190px; right: 0; bottom: 0;
    background: linear-gradient(90deg, var(--silver-dark) 0%, var(--silver) 30%, var(--silver-light) 55%, var(--silver) 80%, var(--silver-dark) 100%);
  }
  .brand-name {
    position: absolute;
    color: var(--white);
    font-weight: 500;
    white-space: nowrap;
  }
  .card--contact .brand-name { left: 34px; top: 102px; font-size: 26px; }
  .person {
    position: absolute; right: 26px; top: 30px;
    display: flex; align-items: center; gap: 8px;
    color: var(--white); font-size: 14px; font-weight: 400;
  }
  .person-name { letter-spacing: 0.03em; text-transform: uppercase; }
  .person-divider { width: 2px; height: 20px; background: var(--hazard-yellow); }
  .contact-list {
    position: absolute; left: 300px; top: 210px;
    list-style: none;
    color: var(--ink); font-size: 12px; line-height: 1.45;
  }
  .contact-list .address { margin-bottom: 4px; }
  .contact-list .item { display: flex; align-items: center; gap: 6px; }
  .contact-list .bullet { width: 5px; height: 5px; background: var(--hazard-yellow); flex: none; }

  /* logo side */
  .card--logo {
    left: 60px; top: 470px;
    background: linear-gradient(170deg, var(--charcoal-light) 0%, var(--charcoal) 50%, var(--charcoal-dark) 100%);
  }
  .card--logo .accent-band--top { top: 0; }
  .card--logo .accent-band--bottom { bottom: 0; }
  .card--logo .brand-name {
    left: 0; right: 0; top: 136px;
    text-align: center;
    font-size: 36px;
  }
</style>
</head>
<body>
  <section class="card card--contact" aria-label="Business card, contact side">
    <div class="contact-top">
      <div class="person">
        <span class="person-name">Mara Thornby</span>
        <span class="person-divider"></span>
        <span class="person-title">Company Director</span>
      </div>
      <span class="brand-name">keelbuild</span>
      <div class="accent-band" role="img" aria-label="Yellow and black hazard stripe band"></div>
    </div>
    <div class="contact-bottom"></div>
    <ul class="contact-list">
      <li class="address">1180 Tidewater Lane #40<br>Harbor Point, WA 98201</li>
      <li class="item"><span class="bullet"></span>hello@keelbuild.com</li>
      <li class="item"><span class="bullet"></span>360 555 0142</li>
      <li class="item"><span class="bullet"></span>360 555 0143</li>
    </ul>
  </section>

  <section class="card card--logo" aria-label="Business card, logo side">
    <div class="accent-band accent-band--top" role="img" aria-label="Yellow and black hazard stripe band"></div>
    <span class="brand-name">keelbuild</span>
    <div class="accent-band accent-band--bottom" role="img" aria-label="Yellow and black hazard stripe band"></div>
  </section>
</body>
</html>
```